Answer Choice Icons

We need four versions of an answer choice icon. We need an A, B, C and D. They need to be 40 by 40 pixels and in .png format. They will be used as the labels for the answer choices on a multiple choice test. The student will click on the A, the B, the C, or D icon to select their answer. I have uploaded an example.

Industry/Entity Type

Student

Requirements
Must have
• 40 x 40 pixels; png format
Nice to have
• An oval shape with some shine would be nice. Also having each one a different color would be good.

```html
<!DOCTYPE html>
<html lang="en">
<head>
<meta charset="utf-8">
<title>Find the Area of the Rectangle</title>
<link rel="stylesheet" href="https://fonts.googleapis.com/css2?family=Tinos:wght@400;700&display=swap">
<style>
  :root {
    --bg: #ffffff;
    --ink: #000000;
    --rule: #e0101a;
    --blue: #4f86d8;
    --green: #3ea43a;
    --orange: #e8930c;
    --gray: #7a7a7a;
    --cell: #000000;
    --gap: #ffffff;
  }
  * { margin: 0; padding: 0; box-sizing: border-box; }
  html, body { width: 1200px; height: 578px; overflow: hidden; background: var(--bg); }
  body { font-family: "Tinos", "Times New Roman", serif; position: relative; }

  .quiz-title {
    position: absolute; left: 0; width: 1172px; top: 38px;
    text-align: center; font-size: 28px; font-weight: 400;
    letter-spacing: 0.6px; color: var(--ink);
  }
  .title-rule {
    position: absolute; left: 232px; top: 79px; width: 708px; height: 2px;
    background: linear-gradient(90deg, rgba(224,16,26,0), var(--rule) 30%, var(--rule) 70%, rgba(224,16,26,0));
  }

  .choices { list-style: none; }
  .choice {
    position: absolute; left: 88px; height: 60px;
    display: flex; align-items: center;
  }
  .choice-letter { width: 66px; font-size: 31px; }
  .choice-icon { width: 68px; height: 56px; }
  .choice-text { margin-left: 31px; font-size: 34px; letter-spacing: 1.4px; }
  .choice--a { top: 120px; color: var(--blue); }
  .choice--b { top: 206px; color: var(--green); }
  .choice--c { top: 291px; color: var(--orange); }
  .choice--d { top: 375px; color: var(--gray); }

  .unit-key {
    position: absolute; left: 609px; top: 286px; height: 42px;
    display: flex; align-items: center; font-size: 34px; letter-spacing: 1.4px; color: var(--ink);
  }
  .unit-square { width: 41px; height: 42px; background: var(--cell); margin-left: 14px; }

  .rectangle-grid {
    position: absolute; left: 997px; top: 67px; width: 130px; height: 432px;
    display: grid; grid-template-columns: repeat(3, 1fr); grid-template-rows: repeat(10, 1fr);
    gap: 3px; background: var(--gap);
    box-shadow: 0 6px 8px rgba(0,0,0,0.25);
  }
  .rectangle-grid span { background: var(--cell); }
</style>
</head>
<body>
  <h1 class="quiz-title">FIND THE AREA OF THE RECTANGLE</h1>
  <div class="title-rule"></div>

  <svg width="0" height="0" style="position:absolute">
    <defs>
      <radialGradient id="shine-blue" cx="50%" cy="65%" r="60%"><stop offset="0" stop-color="#bfe6ff"/><stop offset="0.6" stop-color="#4aa2ea"/><stop offset="1" stop-color="#1c5fb4"/></radialGradient>
      <radialGradient id="shine-green" cx="50%" cy="65%" r="60%"><stop offset="0" stop-color="#b8f5a8"/><stop offset="0.6" stop-color="#3cc23a"/><stop offset="1" stop-color="#137a1a"/></radialGradient>
      <radialGradient id="shine-orange" cx="50%" cy="65%" r="60%"><stop offset="0" stop-color="#ffe27a"/><stop offset="0.6" stop-color="#f5a000"/><stop offset="1" stop-color="#c26a00"/></radialGradient>
      <radialGradient id="shine-gray" cx="50%" cy="65%" r="60%"><stop offset="0" stop-color="#e2e2e2"/><stop offset="0.6" stop-color="#8a8a8a"/><stop offset="1" stop-color="#3e3e3e"/></radialGradient>
      <linearGradient id="gloss" x1="0" y1="0" x2="0" y2="1"><stop offset="0" stop-color="#fff" stop-opacity="0.9"/><stop offset="1" stop-color="#fff" stop-opacity="0.1"/></linearGradient>
      <radialGradient id="drop" cx="50%" cy="50%" r="50%"><stop offset="0" stop-color="#000" stop-opacity="0.3"/><stop offset="1" stop-color="#000" stop-opacity="0"/></radialGradient>
    </defs>
  </svg>

  <ul class="choices">
    <li class="choice choice--a">
      <span class="choice-letter">A</span>
      <svg class="choice-icon" viewBox="0 0 68 56" aria-hidden="true"><ellipse cx="34" cy="50" rx="26" ry="5" fill="url(#drop)"/><ellipse cx="34" cy="27" rx="32" ry="24" fill="url(#shine-blue)"/><ellipse cx="34" cy="13" rx="20" ry="9" fill="url(#gloss)"/></svg>
      <span class="choice-text">30 square meters</span>
    </li>
    <li class="choice choice--b">
      <span class="choice-letter">B</span>
      <svg class="choice-icon" viewBox="0 0 68 56" aria-hidden="true"><ellipse cx="34" cy="50" rx="26" ry="5" fill="url(#drop)"/><ellipse cx="34" cy="27" rx="32" ry="24" fill="url(#shine-green)"/><ellipse cx="34" cy="13" rx="20" ry="9" fill="url(#gloss)"/></svg>
      <span class="choice-text">13 square meters</span>
    </li>
    <li class="choice choice--c">
      <span class="choice-letter">C</span>
      <svg class="choice-icon" viewBox="0 0 68 56" aria-hidden="true"><ellipse cx="34" cy="50" rx="26" ry="5" fill="url(#drop)"/><ellipse cx="34" cy="27" rx="32" ry="24" fill="url(#shine-orange)"/><ellipse cx="34" cy="13" rx="20" ry="9" fill="url(#gloss)"/></svg>
      <span class="choice-text">26 square meters</span>
    </li>
    <li class="choice choice--d">
      <span class="choice-letter">D</span>
      <svg class="choice-icon" viewBox="0 0 68 56" aria-hidden="true"><ellipse cx="34" cy="50" rx="26" ry="5" fill="url(#drop)"/><ellipse cx="34" cy="27" rx="32" ry="24" fill="url(#shine-gray)"/><ellipse cx="34" cy="13" rx="20" ry="9" fill="url(#gloss)"/></svg>
      <span class="choice-text">40 square meters</span>
    </li>
  </ul>

  <div class="unit-key">1 square meters =<span class="unit-square"></span></div>

  <div class="rectangle-grid" role="img" aria-label="Rectangle made of 3 by 10 unit squares">
    <span></span><span></span><span></span><span></span><span></span><span></span>
    <span></span><span></span><span></span><span></span><span></span><span></span>
    <span></span><span></span><span></span><span></span><span></span><span></span>
    <span></span><span></span><span></span><span></span><span></span><span></span>
    <span></span><span></span><span></span><span></span><span></span><span></span>
  </div>
</body>
</html>
```